Meridian Rest Supply Needs Business Card

Looking for a very nice looking business card. Creative but not extravagant. We sell beds and pillows across the U.S. and need something professional but catchy. I have attached the logo.

Name : Dale Fenwick
Title : President
Phone : (800) 417-2964
Email: sleep@quorvana.com
Website: www.quorvana.com

Can be single-sided or double-sided
horizontal or vertical

Can use Blues/Greys

Target Market(s)

Mass Market

Industry/Entity Type

Retail

Contact Information for Business Card

Name : Dale Fenwick
Title : President
Phone : (800) 417-2964
Email: sleep@quorvana.com
Website: www.quorvana.com

Requirements
Must have
• Clean, Modern, Smooth
• Can use Blues/Greys
• On the other side without the information - have something simple like www.quorvana.com or our logo
Nice to have
• Surprise me
Should not have
• Nothing crazy, nothing cluttered

```html
<!DOCTYPE html>
<html lang="en">
<head>
<meta charset="utf-8">
<title>Quorvana Business Card</title>
<link rel="stylesheet" href="https://fonts.googleapis.com/css2?family=Open+Sans:wght@400;700&family=Quicksand:wght@400&display=swap">
<style>
  :root {
    --stage: #dcdde0;
    --navy: #2e3140;
    --navy-deep: #1f2230;
    --navy-soft: #3a3e52;
    --blue-royal: #3f63b0;
    --blue-sky: #7cb8d6;
    --blue-mid: #4f7ba6;
    --blue-light: #6aa0cc;
    --logo-blue: #6aa6d6;
    --paper: #e7e9ed;
    --ink-light: #eef4fa;
    --white: #ffffff;
  }
  html, body {
    margin: 0;
    padding: 0;
    width: 1200px;
    height: 800px;
    overflow: hidden;
    background: var(--stage);
  }
  .canvas {
    position: relative;
    width: 1200px;
    height: 800px;
  }
  .card {
    position: absolute;
    width: 560px;
    height: 320px;
    box-shadow: 0 10px 24px rgba(0,0,0,0.28);
  }
  .card svg { display: block; }
  .card--front { left: 290px; top: 50px; }
  .card--back  { left: 350px; top: 420px; }

  .wordmark {
    font-family: "Quicksand", sans-serif;
    font-weight: 400;
    fill: var(--logo-blue);
  }
  .holder-name {
    font-family: "Open Sans", sans-serif;
    font-weight: 700;
    font-size: 21px;
    fill: var(--white);
  }
  .holder-title {
    font-family: "Open Sans", sans-serif;
    font-weight: 400;
    font-size: 14px;
    fill: var(--logo-blue);
  }
  .contact-line {
    font-family: "Open Sans", sans-serif;
    font-weight: 400;
    font-size: 14px;
    fill: var(--ink-light);
  }
  .icon-stroke { fill: none; stroke: var(--ink-light); stroke-width: 1.2; }
  .icon-fill { fill: var(--ink-light); }
  .fill-navy { fill: var(--navy); }
  .fill-paper { fill: var(--paper); }
</style>
</head>
<body>
<main class="canvas">

  <section class="card card--front" aria-label="Card front">
    <svg width="560" height="320" viewBox="0 0 560 320">
      <defs>
        <radialGradient id="front-ground" cx="55%" cy="50%" r="70%">
          <stop offset="0" stop-color="var(--navy-soft)"/>
          <stop offset="1" stop-color="var(--navy-deep)"/>
        </radialGradient>
        <linearGradient id="band-soft" x1="0" y1="0" x2="1" y2="0">
          <stop offset="0" stop-color="var(--blue-royal)"/>
          <stop offset="1" stop-color="var(--blue-sky)"/>
        </linearGradient>
      </defs>
      <rect class="front-ground" width="560" height="320" fill="url(#front-ground)"/>
      <rect class="band-art band-art--top" x="0" y="0" width="560" height="56" fill="url(#band-soft)" role="img" aria-label="Decorative blue band artwork"/>
      <rect class="band-art band-art--bottom" x="0" y="270" width="560" height="50" fill="url(#band-soft)" role="img" aria-label="Decorative blue band artwork"/>
      <text class="wordmark" x="300" y="178" font-size="66" text-anchor="middle">quorvana</text>
    </svg>
  </section>

  <section class="card card--back" aria-label="Card back">
    <svg width="560" height="320" viewBox="0 0 560 320">
      <defs>
        <linearGradient id="panel-soft" x1="0" y1="0" x2="1" y2="0">
          <stop offset="0" stop-color="var(--blue-mid)"/>
          <stop offset="1" stop-color="var(--blue-light)"/>
        </linearGradient>
      </defs>
      <rect class="fill-navy" width="560" height="320"/>
      <rect class="fill-paper" x="0" y="272" width="560" height="48"/>

      <path class="fold-art" d="M0 212 H250 V150 H560 V272 H0 Z" fill="url(#panel-soft)" role="img" aria-label="Folded paper strip illustration"/>

      <text class="wordmark" x="532" y="74" font-size="40" text-anchor="end">quorvana</text>

      <text class="holder-name" x="48" y="150">Dale Fenwick</text>
      <text class="holder-title" x="50" y="174">President</text>

      <g class="contact-icon contact-icon--phone" transform="translate(318,176)">
        <rect width="14" height="14" rx="3" class="icon-fill" opacity="0.9"/>
        <path d="M4 3.5 L6 3.5 L6.8 6 L5.6 7 Q6.6 8.8 8 9.6 L9 8.4 L11.2 9.2 L11.2 11 Q7 11.2 4 7 Z" fill="var(--blue-light)"/>
      </g>
      <text class="contact-line" x="342" y="188">(800) 417-2964</text>

      <g class="contact-icon contact-icon--globe" transform="translate(318,202)">
        <circle cx="7" cy="7" r="6.5" class="icon-stroke"/>
        <ellipse cx="7" cy="7" rx="3" ry="6.5" class="icon-stroke"/>
        <line x1="0.5" y1="7" x2="13.5" y2="7" class="icon-stroke"/>
      </g>
      <text class="contact-line" x="342" y="214">www.quorvana.com</text>

      <g class="contact-icon contact-icon--mail" transform="translate(318,230)">
        <rect x="0.5" y="0.5" width="14" height="10" class="icon-stroke"/>
        <polyline points="0.5,0.5 7.5,6 14.5,0.5" class="icon-stroke"/>
      </g>
      <text class="contact-line" x="342" y="241">sleep@quorvana.com</text>
    </svg>
  </section>

</main>
</body>
</html>
```